Math Help Website Needs New Design

Looking to refresh the design of my existing site (quillnumberdesk.com) to be easier on the eyes. I am fully capable of doing the HTML coding and have for years, but I don't have the eye for good design, colors, layout, and fonts. This is where I need help!

I need both a new design scheme and a new logo that matches. The overall functionality will be the same as the existing site, and should not be unrecognizable.

Target Market(s)

It should appeal to students (age 13-22) and their parents, so it should NOT be childish in appearance, nor should it be corporate.

Requirements
Must have
• Should be simple, easy-to-navigate, and neither childish nor corporate. I am looking for a design for both the homepage and a similar "content" page. Simple, bold colors are preferred. A logo should be prominent at the top, with a search bar nearby. Below that I need a similar navigational area like I already have. Then, I need about 200px wide ad space on the left of the main body area.

```html
<!DOCTYPE html>
<html lang="en">
<head>
<meta charset="utf-8">
<title>Quill Number Desk – Math Help</title>
<link href="https://fonts.googleapis.com/css2?family=Arimo:wght@400;700&family=Arvo:wght@400;700&display=swap" rel="stylesheet">
<style>
:root{
  --navy:#1e2a5c;
  --steel:#7096bd;
  --paper:#f7fafd;
  --gridline:#cfe0ef;
  --ink:#4a5890;
  --yellow:#ffe000;
  --green:#8dcf2b;
  --cyan:#27a3d5;
  --orange:#f7941d;
  --red:#e8141b;
  --grey:#c9c9c9;
  --text:#2b3a72;
  --muted:#666;
  --white:#fff;
}
*{box-sizing:border-box;margin:0;padding:0}
html,body{width:998px;height:1200px;overflow:hidden}
body{
  position:relative;
  font-family:"Arimo",Arial,sans-serif;color:var(--text);
  background-color:var(--paper);
  background-image:
    linear-gradient(var(--gridline) 1px,transparent 1px),
    linear-gradient(90deg,var(--gridline) 1px,transparent 1px);
  background-size:16px 16px;
  background-position:0 176px;
}
.abs{position:absolute}
.topbar{left:0;top:0;width:998px;height:22px;background:var(--navy)}
.topbar a{position:absolute;right:98px;top:4px;color:var(--white);font-size:12px;font-weight:700;text-decoration:none}
.header{left:0;top:22px;width:998px;height:154px;background:var(--steel)}
.brand{left:96px;top:78px;display:flex;align-items:center;gap:10px}
.brand-dot{width:18px;height:18px;border-radius:50%;background:var(--white)}
.brand-name{font-family:"Arvo",Georgia,serif;font-size:28px;color:var(--white)}
.search{left:730px;top:65px;width:173px;height:23px;background:#b9cbe0;border:1px solid #9fb4cc;border-radius:3px;font-size:10px;color:var(--white);padding:5px 13px}
.search svg{position:absolute;right:6px;top:3px}
.tab{top:113px;height:32px;border-radius:6px 6px 0 0;color:var(--white);font-size:13px;font-weight:700;display:flex;align-items:center;justify-content:center}
.tab-home{left:383px;width:66px;background:var(--yellow)}
.tab-text{left:450px;width:116px;background:var(--green)}
.tab-video{left:567px;width:118px;background:var(--cyan)}
.tab-more{left:686px;width:120px;background:var(--orange)}
.tab-forum{left:807px;width:86px;background:var(--red)}
.navband{left:246px;top:145px;width:660px;height:31px;background:var(--yellow)}
.panel{background:var(--white);box-shadow:0 2px 6px rgba(0,0,0,.15)}
.main{left:246px;top:176px;width:660px;height:516px}
.ad{background:var(--grey);color:var(--white);display:flex;align-items:center;justify-content:center}
.ad span{font-size:36px;transform:rotate(-90deg);white-space:nowrap}
.ad-tall{left:96px;top:196px;width:131px;height:488px}
.ad-short{left:96px;top:706px;width:131px;height:178px}
.heading{font-family:"Arvo",Georgia,serif;font-weight:700;color:var(--ink);letter-spacing:1.5px}
.h-lessons{left:266px;top:185px;font-size:23px}
.thumb{width:191px;height:73px;border-radius:4px}
.label{font-family:"Arvo",Georgia,serif;font-weight:700;font-size:14px;color:var(--ink);letter-spacing:1px}
.more{width:50px;height:14px;background:var(--ink);color:var(--white);font-size:9px;line-height:14px;text-align:center;border-radius:2px}
.peek{left:906px;top:205px;width:86px;height:180px;border-radius:0 30px 20px 0;background:linear-gradient(#e6c7a6,#9ab4d6 55%,#6f8fc0)}
.h-new{left:263px;top:503px;font-size:22px}
.h-disc{left:480px;top:503px;font-size:22px}
.newlist{left:260px;top:547px;width:183px;list-style:none}
.newlist li{font-size:11.5px;height:29.5px;line-height:29px;padding-left:6px;border-bottom:1px solid #7a9cc4}
.date{width:58px;height:42px;background:var(--ink);color:var(--white);font-size:14px;display:flex;align-items:center;justify-content:center;border-radius:4px;box-shadow:4px 4px 0 var(--orange)}
.post{width:335px;font-size:9.5px;color:var(--muted);line-height:12px}
.post b{display:block;font-size:11.5px;font-weight:400;color:var(--text);margin-bottom:1px}
.post i{display:block;font-style:normal;color:var(--orange);font-size:11px}
.ask{left:247px;top:715px;width:656px;height:175px}
.callout{left:263px;top:679px;width:195px;height:50px;background:var(--orange);color:var(--white);font-family:"Arvo",Georgia,serif;font-weight:700;font-size:14px;text-align:center;line-height:19px;padding-top:5px;border-radius:3px;letter-spacing:1px}
.kid{left:262px;top:742px;width:200px;height:140px;border-radius:8px;background:linear-gradient(#eed6bd,#8fb3dc 55%,#3d5488)}
.intro{left:481px;top:740px;width:190px;font-size:10.5px;color:var(--muted);line-height:13px}
.field-label{font-size:10.5px;color:var(--muted)}
.field{width:120px;height:20px;border:1px solid #9fb0cc;border-radius:4px;background:#f3f6fb}
.btn{height:14px;background:var(--ink);color:var(--white);font-size:9.5px;line-height:14px;text-align:center;border-radius:2px}
.question{left:690px;top:727px;width:191px;height:121px;border:1px solid #b9c6d8;border-radius:5px;background:#f7f7f7}
.footer{left:0;top:915px;width:998px;height:220px;background:var(--steel)}
.col{top:933px;color:var(--white);font-size:13px;line-height:21.2px}
.col h3{font-weight:400;font-size:13.5px;margin-bottom:0}
.divider{top:938px;width:1px;height:183px;background:#dfe8f2}
.bottom{left:0;top:1135px;width:998px;height:65px;background:var(--navy);color:var(--white);font-size:12px}
.bottom .links{position:absolute;left:109px;top:8px}
.bottom .copy{position:absolute;left:658px;top:9px}
</style>
</head>
<body>
<div class="abs topbar"><a href="#">REGISTER / SIGN IN</a></div>
<header class="abs header"></header>
<div class="abs brand"><span class="brand-dot"></span><span class="brand-name">quillnumberdesk</span></div>
<div class="abs search">Search the site...
  <svg width="16" height="16" viewBox="0 0 16 16"><circle cx="9" cy="6" r="4.5" fill="none" stroke="#fff" stroke-width="2"/><line x1="5.8" y1="9.2" x2="2" y2="13.5" stroke="#fff" stroke-width="2.5"/></svg>
</div>
<nav>
  <div class="abs tab tab-home"><svg width="20" height="18" viewBox="0 0 20 18"><path d="M10 1 1 9h3v8h4.5v-5h3v5H16V9h3z" fill="#fff"/></svg></div>
  <div class="abs tab tab-text">TEXT LESSONS</div>
  <div class="abs tab tab-video">VIDEO LESSONS</div>
  <div class="abs tab tab-more">MORE SUBJECTS</div>
  <div class="abs tab tab-forum">FORUM</div>
  <div class="abs navband"></div>
</nav>

<div class="abs ad ad-tall"><span>ADVERTISEMENT</span></div>
<div class="abs ad ad-short"><span>AD</span></div>

<main class="abs panel main"></main>
<h2 class="abs heading h-lessons">MATH LESSONS</h2>

<div class="abs thumb" style="left:264px;top:235px;background:linear-gradient(120deg,#d9d9d9,#f4f4f4)" role="img" aria-label="Pencil over handwritten algebra equations"></div>
<div class="abs thumb" style="left:479px;top:235px;background:linear-gradient(120deg,#e7e9ec,#a9b0b8)" role="img" aria-label="Drawing compass on geometry paper"></div>
<div class="abs thumb" style="left:687px;top:235px;background:linear-gradient(120deg,#3a3a3a,#6d6d6d)" role="img" aria-label="Chalkboard with trigonometry graphs"></div>
<div class="abs thumb" style="left:264px;top:350px;background:linear-gradient(120deg,#e9e9e9,#c8c2bb)" role="img" aria-label="Hand writing calculus on paper"></div>
<div class="abs thumb" style="left:479px;top:350px;background:linear-gradient(120deg,#f1f1f1,#d6dccb)" role="img" aria-label="Pen resting on a statistics bar chart"></div>
<div class="abs thumb" style="left:687px;top:350px;background:linear-gradient(#b96b5f,#4c8a3c 45%,#3f7d33 75%,#a8322f)" role="img" aria-label="Baseball stadium with crowd"></div>

<span class="abs label" style="left:265px;top:315px">ALGEBRA</span><span class="abs more" style="left:403px;top:318px">MORE ❯</span>
<span class="abs label" style="left:479px;top:315px">GEOMETRY</span><span class="abs more" style="left:615px;top:318px">MORE ❯</span>
<span class="abs label" style="left:688px;top:315px">TRIGONOMETRY</span><span class="abs more" style="left:827px;top:318px">MORE ❯</span>
<span class="abs label" style="left:265px;top:430px">CALCULUS</span><span class="abs more" style="left:403px;top:432px">MORE ❯</span>
<span class="abs label" style="left:479px;top:430px">STATISTICS</span><span class="abs more" style="left:615px;top:432px">MORE ❯</span>
<span class="abs label" style="left:688px;top:430px">SPORTS MATH</span><span class="abs more" style="left:827px;top:432px">MORE ❯</span>

<div class="abs peek" role="img" aria-label="Illustrated boy with glasses peeking from behind the panel"></div>

<h2 class="abs heading h-new">WHAT'S NEW</h2>
<ul class="abs newlist">
  <li>Multiplying Polynomials</li>
  <li>Derivative of an Inverse Function</li>
  <li>Derivatives of Logs and Exps</li>
  <li>Differentiating Trig Functions</li>
</ul>

<h2 class="abs heading h-disc">CURRENT DISCUSSIONS</h2>
<div class="abs date" style="left:480px;top:550px">12 Jan</div>
<div class="abs post" style="left:549px;top:547px"><b>Comparing Likert scales of different lengths</b><i>Posted by: DataMarlow</i>Hi there math and statistics experts! For my thesis I am doing research about listener's attitudes towards 4 different Dutch accents.</div>
<div class="abs date" style="left:480px;top:616px">6 Jan</div>
<div class="abs post" style="left:549px;top:611px"><b>Time/dist/speed.</b><i>Posted by: Tutorbell</i>a, b and c are three linear towns. c divides the line. It takes Ron 72 mins to travel from a to c. It takes Zak 50 mins to travel from b to c.</div>

<section class="abs panel ask"></section>
<div class="abs kid" role="img" aria-label="Illustrated student lying down writing in a notebook"></div>
<svg class="abs" style="left:290px;top:727px" width="45" height="30" viewBox="0 0 45 30"><path d="M0 0h40L35 28z" fill="#f7941d"/></svg>
<div class="abs callout">ASK YOUR QUESTION<br>MESSAGE BOARD</div>

<p class="abs intro">Register and Sign in to get your questions answered by our friendly Forum volunteers.</p>
<span class="abs field-label" style="left:482px;top:804px">User Name:</span>
<div class="abs field" style="left:544px;top:802px"></div>
<span class="abs field-label" style="left:482px;top:828px">Password:</span>
<div class="abs field" style="left:544px;top:827px"></div>
<div class="abs btn" style="left:483px;top:858px;width:65px">SIGN IN ❯</div>
<div class="abs btn" style="left:590px;top:858px;width:75px">REGISTER ❯</div>
<div class="abs question"></div>
<div class="abs btn" style="left:691px;top:858px;width:138px">SUMBIT YOUR QUESTION ❯</div>

<footer class="abs footer"></footer>
<div class="abs col" style="left:265px">
  <h3>FREE MATH RESOURCES</h3>
  Mr. Arlo's Lessons<br>Algebra Lessons<br>Geometry Lessons<br>Trigonometry Lessons<br>Calculus Lessons<br>Statistics Lessons<br>Sports Math
</div>
<div class="abs divider" style="left:467px"></div>
<div class="abs col" style="left:493px">
  <h3>FREE CALCULATORS HELP</h3>
  Equation Solver<br>Equation Grapher<br>Derivative Calculator<br>Factoring Calculator<br>Integral Calculator
</div>
<div class="abs divider" style="left:695px"></div>
<div class="abs col" style="left:720px">
  <h3>MORE SUBJECTS</h3>
  Ask an Expert<br>Books<br>Calculator Buying Guide<br>Famous Mathematicialns<br>Origins of Math<br>Math Games<br>Glossary<br>Study Tips
</div>
<div class="abs bottom">
  <span class="links">Terms of Use &nbsp;|&nbsp; Privacy Policy &nbsp;|&nbsp; Contact Us &nbsp;|&nbsp; About Us &nbsp;|&nbsp; Download Docuview Reader</span>
  <span class="copy">Quill Number Desk © 2013 All Rights Reserved</span>
</div>
</body>
</html>
```